Business Card Design

Take existing logo/brand and develop business card for sales team.
We have two separate brands and require a business card for each.

1. VoxHarbor
2. MyNimbusLinko

Refer to our websites www.voxharbor.example.au and www.mynimbuslinko.example.au for designs currently implemented and in the marketplace.

Both cards are brands of our parent company Quorra Systems Pty Ltd - an Australian Telecommunications company in the medium business sector. We have only business customers, no retail/residential consumers.

Target Market(s)

Australian Business - small to medium enterprise

Industry/Entity Type

Business

Contact Information for Business Card

Lev Dorrit
Sales Director
Mobile: +61 400 555 187
Direct: +61 3 9555 0137
Email: lev@voxharbor.example.au
VoxHarbor (a brand of Quorra Systems Pty Ltd)

Lev Dorrit
Sales Director
Mobile: +61 400 555 187
Direct: +61 3 9555 0137
Email: lev@mynimbuslinko.example.au
MyNimbusLinko (a brand of Quorra Systems Pty Ltd)

Font styles to use
Sans Serif
Other font styles liked:
• Roboto Condensed, Open Sans

Requirements
Must have
• Clean lines, crisp fonts - suggest Roboto Condensed or similar.
• Must be easy to read and clear.
• Brand colour #0C8CCD
• Two colour maximum
Nice to have
• Modern, intellectual and unique design.
Should not have
• No die cuts
• No copies or rip-offs of other designs

```html
<!DOCTYPE html>
<html lang="en">
<head>
<meta charset="utf-8">
<title>VoxHarbor and MyNimbusLinko business cards</title>
<link rel="stylesheet" href="https://fonts.googleapis.com/css2?family=Open+Sans:wght@400;600&display=swap">
<style>
  :root {
    --brand-blue: #0c8ccd;
    --charcoal: #333333;
    --ink: #3a3a3a;
    --paper: #ffffff;
    --backdrop: #eeeeee;
    --muted-on-blue: rgba(255,255,255,0.7);
    --muted-on-dark: rgba(255,255,255,0.6);
  }
  html, body {
    margin: 0;
    padding: 0;
    overflow: hidden;
  }
  body {
    width: 1200px;
    height: 1000px;
    background: var(--backdrop);
    position: relative;
    font-family: "Open Sans", sans-serif;
  }
  .card {
    position: absolute;
    width: 349px;
    height: 193px;
    box-sizing: border-box;
  }
  .card__frame {
    position: absolute;
    left: 14px;
    top: 12px;
    right: 14px;
    bottom: 12px;
    border: 1px solid var(--brand-blue);
  }
  .card--front { background: var(--paper); }
  .card--back-blue { background: var(--brand-blue); }
  .card--back-dark { background: var(--charcoal); }
  .card--back-blue .card__frame,
  .card--back-dark .card__frame { border-color: var(--paper); }

  .vox-front { left: 158px; top: 60px; }
  .vox-back { left: 158px; top: 276px; }
  .nimbus-front { left: 692px; top: 60px; }
  .nimbus-back { left: 692px; top: 276px; height: 193px; }

  .wordmark {
    position: absolute;
    display: flex;
    align-items: center;
    gap: 6px;
    font-weight: 400;
    white-space: nowrap;
  }
  .wordmark__dot {
    width: 22px;
    height: 22px;
    border-radius: 50%;
  }
  .wordmark__square {
    width: 22px;
    height: 22px;
  }
  .wordmark--centered {
    left: 50%;
    top: 50%;
    transform: translate(-50%, -50%);
    font-size: 21px;
  }
  .wordmark--corner {
    left: 27px;
    top: 22px;
    font-size: 18px;
  }
  .wordmark--corner .wordmark__dot,
  .wordmark--corner .wordmark__square { width: 20px; height: 20px; }

  .vox-front .wordmark { color: var(--brand-blue); }
  .vox-front .wordmark__dot { background: var(--brand-blue); }
  .vox-back .wordmark { color: var(--paper); }
  .vox-back .wordmark__dot { background: var(--paper); }
  .nimbus-front .wordmark { color: var(--ink); }
  .nimbus-front .wordmark__square { background: var(--brand-blue); }
  .nimbus-back .wordmark { color: var(--paper); }
  .nimbus-back .wordmark__square { background: var(--brand-blue); }

  .contact {
    position: absolute;
    left: 27px;
    top: 85px;
    margin: 0;
    font-size: 8.6px;
    line-height: 10.8px;
    color: var(--paper);
  }
  .contact p { margin: 0; }
  .contact .rule { line-height: 10px; }
  .contact .parent-note {
    font-size: 7.4px;
  }
  .vox-back .parent-note { color: var(--muted-on-blue); }
  .nimbus-back .parent-note { color: var(--muted-on-dark); }
</style>
</head>
<body>

  <section class="card card--front vox-front" aria-label="VoxHarbor card front">
    <div class="card__frame"></div>
    <div class="wordmark wordmark--centered">
      <span class="wordmark__dot"></span><span>voxharbor</span>
    </div>
  </section>

  <section class="card card--back-blue vox-back" aria-label="VoxHarbor card back">
    <div class="card__frame"></div>
    <div class="wordmark wordmark--corner">
      <span class="wordmark__dot"></span><span>voxharbor</span>
    </div>
    <div class="contact">
      <p>Lev Dorrit Sales Director</p>
      <p class="rule">–</p>
      <p>Mobile: +61 400 555 187</p>
      <p>Direct: +61 3 9555 0137</p>
      <p>Email: lev@voxharbor.example.au</p>
      <p>Website: voxharbor.example.au</p>
      <p class="rule">–</p>
      <p class="parent-note">VoxHarbor, a brand of Quorra Systems Pty Ltd.</p>
    </div>
  </section>

  <section class="card card--front nimbus-front" aria-label="MyNimbusLinko card front">
    <div class="card__frame"></div>
    <div class="wordmark wordmark--centered">
      <span class="wordmark__square"></span><span>mynimbuslinko</span>
    </div>
  </section>

  <section class="card card--back-dark nimbus-back" aria-label="MyNimbusLinko card back">
    <div class="card__frame"></div>
    <div class="wordmark wordmark--corner">
      <span class="wordmark__square"></span><span>mynimbuslinko</span>
    </div>
    <div class="contact">
      <p>Lev Dorrit Sales Director</p>
      <p class="rule">–</p>
      <p>Mobile: +61 400 555 187</p>
      <p>Direct: +61 3 9555 0137</p>
      <p>Email: lev@mynimbuslinko.example.au</p>
      <p>Website: mynimbuslinko.example.au</p>
      <p class="rule">–</p>
      <p class="parent-note">MyNimbusLinko, a brand of Quorra Systems Pty Ltd.</p>
    </div>
  </section>

</body>
</html>
```